Business Card Design Project

Business is web based; no retail location. Business card needs to direct potential customers to our website.

Target Market(s)

Parents, Adult Fans of Tumvo

Industry/Entity Type

Retail

Requirements
Must have
• Email Address
Website Address
Should not have
• Telephone Number

```html
<!DOCTYPE html>
<html lang="en">
<head>
<meta charset="utf-8">
<title>Harbor Town Blocks – Business Card</title>
<link rel="stylesheet" href="https://fonts.googleapis.com/css2?family=Arimo:wght@400;700&display=swap">
<style>
  :root {
    --page: #1d1d1f;
    --card-light: #f1f1f1;
    --card-light-edge: #dcdcdc;
    --brand-red: #c8161d;
    --brand-red-dark: #9c0f14;
    --brand-yellow: #f2c318;
    --brand-yellow-dark: #e0a511;
    --brand-blue: #3f63d8;
    --brand-blue-light: #1fa3e6;
    --ink: #3a3a3a;
    --rule: #8a8a8a;
    --white: #ffffff;
  }
  * { box-sizing: border-box; margin: 0; padding: 0; }
  html, body { width: 1200px; height: 984px; overflow: hidden; }
  body {
    background: var(--page);
    font-family: "Arimo", Arial, sans-serif;
    position: relative;
  }
  .card {
    position: absolute;
    left: 220px;
    width: 760px;
    height: 434px;
    overflow: hidden;
  }
  .card--back { top: 38px; background: linear-gradient(135deg, var(--brand-blue) 0%, var(--brand-blue) 55%, var(--brand-blue-light) 100%); }
  .card--front { top: 512px; background: linear-gradient(180deg, var(--card-light) 0%, var(--card-light-edge) 100%); }
  .card__bands { position: absolute; inset: 0; width: 760px; height: 434px; }
  .brick-art {
    position: absolute;
    background: linear-gradient(90deg, var(--brand-red) 0%, var(--brand-red) 48%, var(--brand-yellow-dark) 52%, var(--brand-yellow) 100%);
    border-radius: 6px;
  }
  .card--front .brick-art { left: 70px; top: 36px; width: 260px; height: 210px; }
  .card--back .brick-art { left: 250px; top: 22px; width: 260px; height: 190px; }
  .brand-name {
    position: absolute;
    font-weight: 700;
    font-size: 26px;
    line-height: 1;
    white-space: nowrap;
  }
  .card--front .brand-name { left: 70px; top: 262px; color: var(--brand-red-dark); }
  .card--back .brand-name { left: 250px; top: 226px; color: var(--white); }
  .divider {
    position: absolute;
    left: 380px; top: 40px;
    width: 1px; height: 250px;
    background: var(--rule);
  }
  .contact { position: absolute; left: 410px; top: 70px; }
  .contact__name {
    color: var(--brand-red);
    font-weight: 700;
    font-size: 30px;
    line-height: 1.2;
    margin-bottom: 30px;
  }
  .contact__list { list-style: none; color: var(--ink); font-size: 18px; line-height: 26px; }
  .contact__list li { display: flex; align-items: flex-start; gap: 12px; margin-bottom: 8px; }
  .contact__icon { width: 16px; height: 16px; margin-top: 5px; flex: none; fill: var(--ink); }
  .web-line {
    position: absolute;
    right: 34px; top: 300px;
    color: var(--white);
    font-size: 17px;
    white-space: nowrap;
  }
</style>
</head>
<body>

  <section class="card card--back" aria-label="Card back">
    <svg class="card__bands" viewBox="0 0 760 434" aria-hidden="true">
      <path d="M0 330 C 220 320 430 300 760 235 L760 434 L0 434Z" fill="var(--brand-yellow)"/>
      <path d="M0 360 C 260 340 470 300 760 205 L760 434 L0 434Z" fill="var(--brand-red)"/>
      <path d="M0 395 C 260 380 480 350 760 300 L760 434 L0 434Z" fill="var(--brand-red-dark)" opacity="0.35"/>
    </svg>
    <div class="brick-art" role="img" aria-label="Illustration of a red and a yellow toy building brick standing side by side"></div>
    <p class="brand-name">Harbor Town Blocks</p>
    <p class="web-line">www.harbortownblocks.com</p>
  </section>

  <section class="card card--front" aria-label="Card front">
    <svg class="card__bands" viewBox="0 0 760 434" aria-hidden="true">
      <path d="M0 285 C 250 330 500 350 760 345 L760 434 L0 434Z" fill="var(--brand-yellow)"/>
      <path d="M0 300 C 250 348 500 368 760 372 L760 434 L0 434Z" fill="var(--white)"/>
      <path d="M0 306 C 250 356 500 378 760 384 L760 434 L0 434Z" fill="var(--brand-red)"/>
    </svg>
    <div class="brick-art" role="img" aria-label="Illustration of a red and a yellow toy building brick standing side by side"></div>
    <p class="brand-name">Harbor Town Blocks</p>
    <div class="divider"></div>
    <div class="contact">
      <p class="contact__name">Dale Ferrin</p>
      <ul class="contact__list">
        <li>
          <svg class="contact__icon" viewBox="0 0 16 16"><path d="M1 3 H15 V13 H1Z M2 4 L8 9 L14 4" stroke="var(--card-light)" stroke-width="1"/></svg>
          <span>dale@harbortownblocks.com</span>
        </li>
        <li>
          <svg class="contact__icon" viewBox="0 0 16 16"><circle cx="8" cy="8" r="7"/><path d="M1 8 H15 M8 1 V15 M3 4 H13 M3 12 H13" stroke="var(--card-light)" stroke-width="1" fill="none"/></svg>
          <span>www.harbortownblocks.com</span>
        </li>
      </ul>
    </div>
  </section>

</body>
</html>
```